依頼詳細
デザインをお願いする当サイトのトップページの役割は、
・当該部門の抽象的イメージの表現
・各種コンテンツ(製品情報、ブログ記事)のポータル的機能
の2つを主軸に据えようと考えています。

デザインの条件として、
・サイトロゴはこちから指定したものを使用する。
・レスポンシブデザインを適用する。
とさせて頂きます。ついては、

開発したアプリ、サービス等の周知、蓄積した技術情報等の発信を行うためにWebサイトとして見栄えがする、
・ページ全体、および個々の要素の配色
・ボーダー、シャドウのデザイン
・各要素の質感
のデザインをご提案頂きたいです。

現在、こちらで添付のようなページレイアウトを検討していますが、あくまで案ですので、レイアウトも含めたデザインをご提案いただいても構いません。
ページ数
1ページ
希望イメージ
シンプル 複雑
単色 カラフル
暗い 明るい
日常 高級
遊び心 厳粛
未来的 伝統的
女性的 男性的
希望する色
ロゴのカラーバリエーションのいずれかにマッチする配色でお願いします。
納品ファイル
• 高解像度JPG (.jpg)
• イラストレーター形式 (.ai)
• フォトショップ形式 (.psd)
• PNG形式 (.png)
補足説明
ロゴには、カラーバリエーションがありますので、サイト全体の配色に合うものを
適宜選択していただければと思います。
〆切を延長させて頂きます。

シンプルでわかりやすいデザインがサイトにマッチすると思いました。

たくさんのご提案をありがとうございます。
今後ともよろしくお願いします。

```html
<!DOCTYPE html>
<html lang="ja">
<head>
<meta charset="utf-8">
<title>NovaLab</title>
<link href="https://fonts.googleapis.com/css2?family=Open+Sans:wght@300;400;600&family=Noto+Sans+JP:wght@400;500&display=swap" rel="stylesheet">
<style>
:root{
  --teal:#17b3ad;
  --teal-dark:#0f9c97;
  --blue:#2a9fd8;
  --page:#eef3f6;
  --ink:#333a40;
  --muted:#8a949b;
  --white:#ffffff;
  --hero-a:#1c2a3a;
  --hero-b:#5d7a92;
}
*{margin:0;padding:0;box-sizing:border-box}
html,body{width:1200px;height:3328px;overflow:hidden}
body{font-family:"Noto Sans JP","Open Sans",sans-serif;background:var(--page);color:var(--ink);position:relative}
.brand{display:flex;align-items:center;gap:12px;font-family:"Open Sans",sans-serif;font-weight:600;color:var(--white)}
.brand .dot{border-radius:50%;background:var(--white)}

.hero{position:absolute;left:0;top:0;width:1200px;height:772px;background:linear-gradient(160deg,var(--hero-a) 0%,var(--hero-b) 55%,#9fb4c4 100%)}
.hero-top{position:absolute;left:0;top:0;width:1200px;height:88px;background:rgba(10,20,30,.45)}
.hero-top .brand{position:absolute;left:40px;top:24px;font-size:32px}
.hero-top .brand .dot{width:26px;height:26px}
.hero-tagline{position:absolute;left:328px;top:28px;font-family:"Open Sans",sans-serif;font-size:15px;line-height:20px;color:var(--white);letter-spacing:.5px}
.hero-mark{position:absolute;left:100px;top:460px;font-size:64px}
.hero-mark .dot{width:48px;height:48px}
.scroll-down{position:absolute;left:552px;top:636px}

.nav{position:absolute;left:0;top:772px;width:1200px;height:108px;background:var(--teal);display:flex;align-items:center;justify-content:space-between;padding:0 48px}
.nav .brand{font-size:36px}
.nav .brand .dot{width:28px;height:28px}
.nav ul{list-style:none;display:flex;gap:40px;font-family:"Open Sans",sans-serif;font-size:15px;font-weight:600;color:var(--white)}

.section-title{position:absolute;left:0;width:1200px;text-align:center;font-family:"Open Sans",sans-serif;font-weight:300;font-size:72px;color:#4a4f54;letter-spacing:1px}

.products{position:absolute;left:0;top:1168px;width:1200px;display:flex}
.product{width:400px}
.product-photo{height:400px}
.product-caption{height:80px;padding:16px 32px;font-size:14px;line-height:22px;color:var(--white)}
.c-blue{background:var(--blue)}
.c-teal{background:var(--teal)}

.blog-grid{position:absolute;left:48px;top:1928px;width:1104px;display:grid;grid-template-columns:repeat(3,352px);column-gap:24px;row-gap:28px}
.post{background:var(--white);height:292px}
.post-photo{height:220px}
.post-meta{display:flex;justify-content:space-between;align-items:center;height:72px;padding:0 28px;font-size:17px}
.post-meta time{font-size:14px;color:var(--muted);font-family:"Open Sans",sans-serif}

.to-top{position:absolute;left:1080px;top:2620px;width:72px;height:72px;background:#111;display:flex;align-items:center;justify-content:center}

.contact{position:absolute;left:0;top:2732px;width:1200px;height:348px;background:linear-gradient(180deg,#2e3c48 0%,#45525c 100%)}
.contact-btn{position:absolute;left:420px;top:2872px;width:360px;height:68px;border:2px solid var(--white);display:flex;align-items:center;justify-content:center;gap:14px;color:var(--white);font-size:18px}

.footer{position:absolute;left:0;top:3080px;width:1200px;height:248px;background:var(--teal);color:var(--white)}
.footer .brand{position:absolute;left:48px;top:32px;font-size:36px}
.footer .brand .dot{width:28px;height:28px}
.footer-text{position:absolute;left:48px;top:100px;font-size:15px;line-height:26px}
.footer-links{position:absolute;right:48px;top:36px;display:flex;gap:32px;font-size:14px;list-style:none}
.copyright{position:absolute;left:0;top:3260px;width:1200px;text-align:center;font-size:13px;font-family:"Open Sans",sans-serif;color:var(--white)}
</style>
</head>
<body>

<header class="hero" role="img" aria-label="Business person touching a glowing digital interface with charts and a world map">
  <div class="hero-top">
    <div class="brand"><span class="dot"></span>NovaLab</div>
    <p class="hero-tagline">TEXTTEXTTEXTTEXTTEXTTEXTTEXTTEXTTEXTTEXTTEXT<br>TEXTTEXTTEXTTEXTTEXTTEXTTEXT</p>
  </div>
  <div class="brand hero-mark"><span class="dot"></span>NovaLab</div>
  <svg class="scroll-down" width="96" height="96" viewBox="0 0 96 96" aria-hidden="true">
    <circle cx="48" cy="48" r="44" fill="none" stroke="#fff" stroke-width="2" opacity=".8"/>
    <path d="M48 30v34M36 52l12 12 12-12" fill="none" stroke="#fff" stroke-width="2"/>
  </svg>
</header>

<nav class="nav">
  <div class="brand"><span class="dot"></span>NovaLab</div>
  <ul><li>HOME</li><li>PRODUCTS</li><li>BLOG</li><li>CONTACT</li></ul>
</nav>

<h2 class="section-title" style="top:1008px">PRODUCTS</h2>
<section class="products">
  <article class="product">
    <div class="product-photo" role="img" aria-label="Laptop and tablet on a desk" style="background:linear-gradient(135deg,#e9edf0,#9aa5ad)"></div>
    <p class="product-caption c-blue">テキストが入ります。テキストが入ります。テキストが入ります。テキストが入ります。</p>
  </article>
  <article class="product">
    <div class="product-photo" role="img" aria-label="Colorful cloud of app and media icons" style="background:radial-gradient(circle at 50% 50%,#f4b53c 0%,#e56a8c 35%,#5cb6e0 65%,#ffffff 90%)"></div>
    <p class="product-caption c-teal">テキストが入ります。テキストが入ります。テキストが入ります。テキストが入ります。</p>
  </article>
  <article class="product">
    <div class="product-photo" role="img" aria-label="Glass globe on a keyboard beside a smartphone" style="background:linear-gradient(135deg,#cfd6db,#5e6a72)"></div>
    <p class="product-caption c-blue">テキストが入ります。テキストが入ります。テキストが入ります。テキストが入ります。</p>
  </article>
</section>

<h2 class="section-title" style="top:1772px">BLOG</h2>
<section class="blog-grid">
  <article class="post"><div class="post-photo" role="img" aria-label="Meeting at a table with documents" style="background:linear-gradient(135deg,#dfe3e6,#8c949a)"></div><div class="post-meta"><span>ブログタイトル</span><time>2015.2.15</time></div></article>
  <article class="post"><div class="post-photo" role="img" aria-label="Person with earphones holding a phone" style="background:linear-gradient(135deg,#d8eef5,#58b4d6)"></div><div class="post-meta"><span>ブログタイトル</span><time>2015.2.15</time></div></article>
  <article class="post"><div class="post-photo" role="img" aria-label="Coffee cup and smartphone on a table" style="background:linear-gradient(135deg,#e6ded4,#7a6a5a)"></div><div class="post-meta"><span>ブログタイトル</span><time>2015.2.15</time></div></article>
  <article class="post"><div class="post-photo" role="img" aria-label="Person outdoors under a blue sky" style="background:linear-gradient(180deg,#6fb7e8,#b9d9a0)"></div><div class="post-meta"><span>ブログタイトル</span><time>2015.2.15</time></div></article>
  <article class="post"><div class="post-photo" role="img" aria-label="Desktop, laptop, tablet and phone showing a blue screen" style="background:linear-gradient(180deg,#f4f6f8,#4a90c8)"></div><div class="post-meta"><span>ブログタイトル</span><time>2015.2.15</time></div></article>
  <article class="post"><div class="post-photo" role="img" aria-label="Hands holding a phone by a lake" style="background:linear-gradient(180deg,#bcd8e6,#9c8a6a)"></div><div class="post-meta"><span>ブログタイトル</span><time>2015.2.15</time></div></article>
</section>

<div class="to-top" aria-label="Back to top">
  <svg width="28" height="28" viewBox="0 0 28 28" aria-hidden="true"><path d="M14 24V5M7 12l7-7 7 7" fill="none" stroke="#fff" stroke-width="2.5"/></svg>
</div>

<section class="contact" role="img" aria-label="Dim photo of people working at laptops"></section>
<a class="contact-btn">
  <svg width="24" height="24" viewBox="0 0 24 24" aria-hidden="true"><circle cx="12" cy="12" r="9" fill="none" stroke="#fff" stroke-width="2"/></svg>
  お問い合わせ
</a>

<footer class="footer">
  <div class="brand"><span class="dot"></span>NovaLab</div>
  <p class="footer-text">テキストが入ります。テキストが入ります。テキストが入ります。<br>テキストが入ります。テキストが入ります。</p>
  <ul class="footer-links"><li>&gt; 事業会社</li><li>&gt; お問い合わせ</li></ul>
</footer>
<p class="copyright">Copyright (C) NovaLab All Right Reserved.</p>

</body>
</html>
```